Business Card Revision

Need to redesign my business cards for a new professional look. We are a courier company. You can go to www.qvrunners.com to see what we do. The trucks have an old company name (Sprout) on them but that is the company we are just now
changing the name.

Target Market(s)

Potential clients. We service the automotive, plumbing, printing, air freight industries as well as many others.

Industry/Entity Type

Business

Contact Information for Business Card

QVmotion
20864 Lark Fenmore Parkway
Brookvale, Ky 45241

Thomas R. Wendall
President

tom@qvrunners.com

Main: (513) 555-0147

```html
<!DOCTYPE html>
<html lang="en">
<head>
<meta charset="utf-8">
<title>QV Runners Business Card</title>
<link href="https://fonts.googleapis.com/css2?family=Open+Sans:wght@400;600;700&display=swap" rel="stylesheet">
<style>
  :root {
    --page-bg: #e4e4e8;
    --card-bg: #ffffff;
    --blue-deep: #1f6fae;
    --blue-bright: #2588c4;
    --ink: #222428;
  }
  * { margin: 0; padding: 0; box-sizing: border-box; }
  html, body {
    width: 1200px;
    height: 720px;
    overflow: hidden;
    background: var(--page-bg);
    font-family: "Open Sans", Arial, sans-serif;
  }
  .card {
    position: absolute;
    top: 223px;
    width: 465px;
    height: 266px;
    background: var(--card-bg);
    color: var(--ink);
  }
  .card--deep { left: 104px; --accent: var(--blue-deep); }
  .card--bright { left: 630px; --accent: var(--blue-bright); }

  .brand {
    position: absolute;
    left: 37px;
    top: 118px;
    display: flex;
    align-items: center;
    gap: 9px;
  }
  .brand__square {
    width: 22px;
    height: 22px;
    background: var(--accent);
  }
  .brand__name {
    font-weight: 700;
    font-size: 22px;
    letter-spacing: 0.3px;
    color: var(--accent);
    white-space: nowrap;
  }

  .contact {
    position: absolute;
    left: 258px;
    top: 76px;
    font-size: 12px;
    line-height: 14px;
  }
  .contact__name {
    font-weight: 700;
    font-size: 14.5px;
    line-height: 16px;
    color: var(--accent);
    text-transform: uppercase;
    letter-spacing: 0.2px;
  }
  .contact__title { margin-bottom: 15px; }
  .contact__address { margin-bottom: 7px; }
  .contact__line {
    display: flex;
    align-items: center;
    gap: 5px;
    margin-bottom: 3px;
  }
  .contact__icon { width: 11px; height: 9px; fill: var(--accent); }
</style>
</head>
<body>

<div class="card card--deep">
  <div class="brand">
    <span class="brand__square"></span>
    <span class="brand__name">QV RUNNERS</span>
  </div>
  <div class="contact">
    <p class="contact__name">Thomas R. Wendall</p>
    <p class="contact__title">President</p>
    <p class="contact__address">20864 Lark Fenmore Parkway<br>Brookvale, Ky 41873</p>
    <p class="contact__line">
      <svg class="contact__icon" viewBox="0 0 11 9" aria-hidden="true"><path d="M0 3 Q5.5 -1 11 3 L9 4 L8 2.5 L3 2.5 L2 4 Z M2.5 4.5 L3.5 3 L7.5 3 L8.5 4.5 L9 9 L2 9 Z"/></svg>
      (555) 410-0147
    </p>
    <p class="contact__line">
      <svg class="contact__icon" viewBox="0 0 11 9" aria-hidden="true"><path d="M0 1 L5.5 5 L11 1 L11 8 L0 8 Z M0.5 0.5 L10.5 0.5 L5.5 4 Z"/></svg>
      tom@qvrunners.com
    </p>
  </div>
</div>

<div class="card card--bright">
  <div class="brand">
    <span class="brand__square"></span>
    <span class="brand__name">QV RUNNERS</span>
  </div>
  <div class="contact">
    <p class="contact__name">Thomas R. Wendall</p>
    <p class="contact__title">President</p>
    <p class="contact__address">20864 Lark Fenmore Parkway<br>Brookvale, Ky 41873</p>
    <p class="contact__line">
      <svg class="contact__icon" viewBox="0 0 11 9" aria-hidden="true"><path d="M0 3 Q5.5 -1 11 3 L9 4 L8 2.5 L3 2.5 L2 4 Z M2.5 4.5 L3.5 3 L7.5 3 L8.5 4.5 L9 9 L2 9 Z"/></svg>
      (555) 410-0147
    </p>
    <p class="contact__line">
      <svg class="contact__icon" viewBox="0 0 11 9" aria-hidden="true"><path d="M0 1 L5.5 5 L11 1 L11 8 L0 8 Z M0.5 0.5 L10.5 0.5 L5.5 4 Z"/></svg>
      tom@qvrunners.com
    </p>
  </div>
</div>

</body>
</html>
```